Business card for law firm

Need business card for new law firm. Think confident, authoritative, conservative, but not stuffy or old-fashioned.

Contact Information for Business Card

Content for card - logo (uploaded), plus the following:

Paul Weybridge (larger font)
Managing Partner (larger font, but not as large as name)
Level 9, 47 Calder Lane
Sydney NSW 2000
Main Tel 02 7304 6219
Direct Tel 02 7462 3158
Email paul@wbrlegal.com.au
www.wbrlegal.com.au

Letterhead design should include logo plus:
Level 9, 47 Calder Lane
Sydney NSW 2000
Tel 02 7462 3158
www.wbrlegal.com.au

```html
<!DOCTYPE html>
<html lang="en">
<head>
<meta charset="utf-8">
<title>Weybridge Lawyers – Business Card</title>
<link rel="stylesheet" href="https://fonts.googleapis.com/css2?family=Cinzel:wght@400&family=Roboto:wght@400;700&display=swap">
<style>
  :root {
    --navy: #0d1f5c;
    --navy-deep: #0a1a4f;
    --ink: #1c1c1c;
    --paper: #ffffff;
    --grey: #c8c8c8;
    --stage: #4a4a4a;
  }
  * { box-sizing: border-box; margin: 0; padding: 0; }
  html, body { width: 1200px; height: 1000px; overflow: hidden; }
  body {
    background: var(--stage);
    position: relative;
    font-family: "Roboto", Arial, sans-serif;
  }
  .card {
    position: absolute;
    width: 560px;
    height: 320px;
    border-radius: 22px;
    overflow: hidden;
  }

  /* Front */
  .card--front {
    left: 580px; top: 110px;
    background: var(--navy);
    color: var(--paper);
  }
  .card--front .brand {
    position: absolute;
    right: 48px; top: 130px;
    display: flex; align-items: center; gap: 14px;
  }
  .brand__square {
    width: 22px; height: 22px;
    background: currentColor;
  }
  .brand__name {
    font-family: "Cinzel", Georgia, serif;
    font-weight: 400;
    font-size: 30px;
    letter-spacing: 1px;
  }
  .card--front .web {
    position: absolute;
    right: 60px; bottom: 50px;
    font-size: 15px;
    letter-spacing: 0.5px;
  }

  /* Back */
  .card--back {
    left: 80px; top: 500px;
    background: var(--paper);
    color: var(--ink);
  }
  .card--back .edge {
    position: absolute; left: 0; top: 0; bottom: 0;
    width: 30px;
    background: var(--navy);
    border-right: 4px solid #111;
  }
  .card--back .corner {
    position: absolute; right: 0; bottom: 0;
    width: 210px; height: 50px;
    background: var(--grey);
    border-top-left-radius: 40px;
  }
  .card--back .brand {
    position: absolute; left: 62px; top: 40px;
    display: flex; align-items: center; gap: 12px;
    color: var(--ink);
  }
  .card--back .brand__square { background: var(--navy); width: 20px; height: 20px; }
  .card--back .brand__name { font-size: 26px; }
  .contact {
    position: absolute; left: 62px; top: 120px;
  }
  .contact__name {
    color: var(--navy);
    font-weight: 700;
    font-size: 22px;
    text-transform: uppercase;
    line-height: 1.1;
  }
  .contact__role {
    font-size: 15px;
    margin-bottom: 10px;
  }
  .contact__line {
    font-size: 14px;
    line-height: 1.4;
  }
  .contact__label { color: var(--navy); font-weight: 700; }
  .contact__line svg { vertical-align: -2px; margin-right: 6px; }
  .card--back .web {
    position: absolute; right: 24px; bottom: 16px;
    font-size: 14px; color: var(--ink);
  }
  .web strong { color: var(--navy); }
</style>
</head>
<body>
  <section class="card card--front" aria-label="Card front">
    <div class="brand">
      <span class="brand__square"></span>
      <span class="brand__name">WEYBRIDGE LAWYERS</span>
    </div>
    <p class="web">www.wbrlegal.com.au</p>
  </section>

  <section class="card card--back" aria-label="Card back">
    <div class="edge"></div>
    <div class="corner"></div>
    <div class="brand">
      <span class="brand__square"></span>
      <span class="brand__name">WEYBRIDGE LAWYERS</span>
    </div>
    <div class="contact">
      <p class="contact__name">Paul Weybridge</p>
      <p class="contact__role">Managing Partner</p>
      <p class="contact__line">Level 9, 47 Calder Lane Sydney NSW 2000</p>
      <p class="contact__line"><span class="contact__label">Main Tel</span> 02 7304 6219</p>
      <p class="contact__line"><span class="contact__label">Direct Tel</span> 02 7462 3158</p>
      <p class="contact__line">
        <svg width="14" height="11" viewBox="0 0 14 11" aria-hidden="true">
          <rect x="0.5" y="0.5" width="13" height="10" fill="#0d1f5c"/>
          <polyline points="1,1 7,6 13,1" fill="none" stroke="#fff" stroke-width="1.2"/>
        </svg>paul@wbrlegal.com.au
      </p>
    </div>
    <p class="web">www.<strong>wbrlegal.com</strong>.au</p>
  </section>
</body>
</html>
```